We need a DL size flyer, double sided, for our lawn mowing and gardening business, Kestrel Yards.

We want to run on the front side, the following promotion:
50% off lawn mowing, applies to first lawn mowed on any regular service,
applies to first 100 callers only, so call now!
Professional lawn mowing at an affordable price.

Logo at the bottom left, with Lawn and Garden Maintenance written just below logo.

On bottom Right contact details;
Tom and Gareth
Ph: 0487650912
Email: kestrelyards@mailbox-demo.com
www.kestrelyards-demo.com.au

Front side positioned horizontally, with a bright and colour full design in the background, with the offer of 50% Off lawn mowing in large letters along the top.

On the rear side, also positioned horizontally, a list of our services, stating;

At Kestrel Yards we specialise in the following services;
Lawn mowing
Edging
Blowing
Hedging
Pruning
Tree Loping
Weeding
Poisoning
Mulching
Fertilising
Rubbish removal
Planting
Lawn care and advice
Turf
And any other garden maintenance job,
No job too big or too small.
(No particular order, whatever fits best)
Also include our contact details,
Kestrel Yards
Ph 0487650912
www.kestrelyards-demo.com.au

Target Market(s)

Home owners, aged between 30-50 years old, moderate socio ecenomic status to more afluent areas.

Industry/Entity Type

Business

Requirements
Must have
• DL size, front and back, full colour.
Nice to have
• The writting stating "Kestrel Yards" in our logo is quite bland, if that could also be amended to make it more appealing, but change the writting design only not the actual logo.

```html
<!DOCTYPE html>
<html lang="en">
<head>
<meta charset="utf-8">
<title>Kestrel Yards – 50% Off Lawn Mowing</title>
<link rel="stylesheet" href="https://fonts.googleapis.com/css2?family=Archivo+Black&family=Arimo:wght@700&family=Roboto+Condensed:wght@700&display=swap">
<style>
  :root {
    --sky-deep: #123f9e;
    --sky-mid: #2a6fd0;
    --sky-light: #5fa6ea;
    --grass-light: #9fce5a;
    --grass-mid: #6fa635;
    --grass-deep: #3f7a1d;
    --band-light: #b4dd6a;
    --band-dark: #74bb2c;
    --offer-green: #86d323;
    --offer-edge: #2d5a10;
    --white: #ffffff;
    --ink: #1f3512;
    --shadow: rgba(10, 30, 70, 0.75);
  }
  * { margin: 0; padding: 0; box-sizing: border-box; }
  html, body { width: 1200px; height: 571px; overflow: hidden; background: #ffffff; }
  .flyer {
    position: relative;
    width: 1200px;
    height: 571px;
    overflow: hidden;
    font-family: "Arimo", Arial, sans-serif;
    font-weight: 700;
  }
  .scenery {
    position: absolute;
    left: 0; top: 0;
    width: 1200px; height: 443px;
    background: linear-gradient(180deg,
      var(--sky-deep) 0%,
      var(--sky-mid) 35%,
      var(--sky-light) 60%,
      var(--grass-light) 64%,
      var(--grass-mid) 80%,
      var(--grass-deep) 100%);
  }
  .offer-amount {
    position: absolute;
    left: 98px; top: 104px;
    font-family: "Archivo Black", "Arial Black", sans-serif;
    font-weight: 400;
    font-size: 62px;
    line-height: 1;
    word-spacing: -8px;
    color: var(--offer-green);
    transform: rotate(-12deg);
    transform-origin: left bottom;
    text-shadow: 3px 4px 0 var(--offer-edge), 6px 8px 8px rgba(0,0,0,0.55);
    white-space: nowrap;
  }
  .offer-title {
    position: absolute;
    left: 434px; top: 48px;
    font-size: 58px;
    font-weight: 700;
    line-height: 1;
    letter-spacing: 1px;
    color: var(--white);
    text-shadow: 3px 4px 5px var(--shadow);
    white-space: nowrap;
  }
  .offer-terms {
    position: absolute;
    left: 442px;
    color: var(--white);
    white-space: nowrap;
    text-shadow: 2px 2px 3px var(--shadow);
    line-height: 1;
  }
  .offer-terms--service { top: 127px; font-size: 22px; letter-spacing: 0.3px; }
  .offer-terms--callers { top: 169px; font-size: 25px; letter-spacing: 0.6px; }
  .call-line {
    position: absolute;
    left: 443px; top: 214px;
    color: var(--white);
    font-family: "Roboto Condensed", "Arial Narrow", sans-serif;
    white-space: nowrap;
    text-shadow: 3px 4px 5px var(--shadow);
    line-height: 1;
    display: flex;
    align-items: baseline;
  }
  .call-line__label { font-size: 50px; margin-right: 20px; }
  .call-line__number { font-size: 74px; letter-spacing: 0.5px; }
  .footer-band {
    position: absolute;
    left: 0; top: 443px;
    width: 1200px; height: 128px;
    background: linear-gradient(90deg, var(--band-light) 0%, var(--band-dark) 100%);
  }
  .brand {
    position: absolute;
    left: 56px; top: 520px;
    display: flex;
    align-items: center;
    gap: 10px;
  }
  .brand__mark {
    width: 22px; height: 22px;
    background: var(--ink);
  }
  .brand__name {
    font-size: 20px;
    color: var(--ink);
    white-space: nowrap;
  }
  .contact {
    position: absolute;
    left: 834px; top: 464px;
    color: var(--ink);
    font-family: "Roboto Condensed", "Arial Narrow", sans-serif;
    font-style: normal;
    white-space: nowrap;
    line-height: 1;
  }
  .contact__names { font-size: 25px; letter-spacing: 1.2px; margin-bottom: 16px; }
  .contact__line { font-size: 18px; letter-spacing: 1px; margin-bottom: 14px; }
</style>
</head>
<body>
  <main class="flyer">
    <div class="scenery" role="img" aria-label="Photo of a lush green lawn under a bright blue sky with light clouds and butterflies"></div>

    <div class="offer-amount">50% OFF</div>
    <h1 class="offer-title">on LAWN MOWING</h1>
    <p class="offer-terms offer-terms--service">applies to first lawn mowed on any regular service</p>
    <p class="offer-terms offer-terms--callers">first 100 callers only, so</p>
    <p class="call-line"><span class="call-line__label">CALL NOW</span><span class="call-line__number">0487650912</span></p>

    <footer class="footer-band"></footer>

    <div class="brand">
      <span class="brand__mark"></span>
      <span class="brand__name">Kestrel Yards</span>
    </div>

    <address class="contact">
      <p class="contact__names">Tom and Gareth</p>
      <p class="contact__line">Email: kestrelyards@mailbox-demo.com</p>
      <p class="contact__line">www.kestrelyards-demo.com.au</p>
    </address>
  </main>
</body>
</html>
```